Redesign for a start up airline technology. The website is tembrulon.com.

I need a PowerPoint template that complements our website. I can provide our current template as a starting point.

```html
<!DOCTYPE html>
<html lang="en">
<head>
<meta charset="utf-8">
<title>Tembrulon Presentation Template</title>
<link href="https://fonts.googleapis.com/css2?family=Montserrat:wght@400;500;600;700;800&display=swap" rel="stylesheet">
<style>
:root{
  --bg:#dddcdd;
  --navy:#1b4d9c;
  --blue:#1d5ea8;
  --sky:#1b78bd;
  --green:#2e8a3c;
  --lime:#6cc04a;
  --ink:#3a3d42;
  --grey:#54575c;
  --white:#ffffff;
}
*{margin:0;padding:0;box-sizing:border-box}
html,body{width:1200px;height:2765px;overflow:hidden}
body{background:var(--bg);font-family:"Montserrat",sans-serif;color:var(--ink);position:relative}
.slide{position:absolute;width:540px;height:304px;background:var(--white);overflow:hidden}
.hero{left:160px;top:86px;transform:scale(1.6296);transform-origin:0 0}
.brand{position:absolute;display:flex;align-items:center;gap:4px;font-weight:800;color:var(--navy);letter-spacing:.5px}
.brand i{display:block;border-radius:50%;background:var(--lime)}
.brand-lg{left:38px;top:24px;font-size:22px}
.brand-lg i{width:9px;height:9px}
.brand-sm{right:20px;top:27px;font-size:12px}
.brand-sm i{width:5px;height:5px}
.brand-w{color:var(--white)}
.band{position:absolute;left:0;top:66px;width:540px;height:215px}
.band-green{background:linear-gradient(90deg,#1c4c9a 0%,#1f5c90 45%,#2c8a3d 100%)}
.band-blue{background:linear-gradient(90deg,#1b4a96 0%,#1c62a8 55%,#1b7cc0 100%)}
.cover-title{position:absolute;left:57px;top:112px;color:var(--white);font-weight:800;font-size:28px;line-height:33px;letter-spacing:.5px}
.cover-sub{position:absolute;left:56px;top:184px;color:var(--white);font-size:12.5px}
.cover-date{position:absolute;left:56px;top:222px;color:var(--white);font-size:6.5px}
.copy-center{position:absolute;left:0;width:540px;top:288px;text-align:center;font-size:5px;color:var(--grey)}
.thanks{position:absolute;left:60px;top:114px;color:var(--white);font-weight:800;font-size:22px}
.contact-h{position:absolute;left:60px;top:163px;color:var(--white);font-weight:700;font-size:9px;letter-spacing:.5px}
.contact{position:absolute;left:60px;top:182px;color:var(--white);font-size:7px;line-height:16px}
.contact div{display:flex;align-items:center;gap:6px}
.contact svg{width:9px;height:9px}
.h{position:absolute;font-weight:800;font-size:17px;color:var(--navy)}
.h-white{color:var(--white)}
.rule{position:absolute;width:44px;height:4px;border-radius:2px;background:linear-gradient(90deg,var(--lime),#cfe9c3)}
.foot-l{position:absolute;left:15px;top:282px;font-size:5px;color:var(--ink)}
.foot-r{position:absolute;right:15px;top:280px;font-size:5px;color:var(--grey);display:flex;align-items:center;gap:5px}
.pg{display:inline-flex;width:9px;height:9px;background:var(--navy);color:var(--white);font-size:4.5px;align-items:center;justify-content:center;border-radius:1px}
.body{position:absolute;font-size:7px;line-height:8px;color:var(--ink)}
.body p{margin-bottom:5px}
.photo{position:absolute}
.gradbox{position:absolute;background:linear-gradient(90deg,#1c4c9a,#2d8a3c);color:var(--white);font-size:6.5px;line-height:7.4px}
.top-band{position:absolute;left:0;top:0;width:540px;background:linear-gradient(90deg,#1c4c9a,#2d8a3c)}
.leader{position:absolute;top:73px;width:74px;text-align:center}
.leader .pic{width:70px;height:100px;margin:0 auto;background:linear-gradient(#cfd0d2,#6d7075);border:1px solid #bbb}
.leader b{display:block;margin-top:6px;font-size:8px;color:var(--navy)}
.leader em{display:block;font-style:normal;font-size:5px;color:var(--green);margin-top:2px}
.leader span{display:block;font-size:5px;line-height:5.6px;margin-top:4px}
.col-h{position:absolute;font-weight:700;font-size:10px;color:var(--green)}
.bul{position:absolute;font-size:5.8px;line-height:6.4px;padding-left:8px}
.bul li{margin-bottom:2px}
.lorem{position:absolute;left:30px;top:80px;width:482px;font-size:5.6px;line-height:6.2px;color:var(--ink);text-align:justify}
.lorem p{margin-bottom:3px}
.graybar{position:absolute;left:0;top:114px;width:283px;height:40px;background:#555a5f;color:var(--white);font-size:7px;line-height:8px;padding:11px 0 0 40px}
</style>
</head>
<body>

<!-- Hero cover -->
<section class="slide hero">
  <div class="brand brand-lg"><i></i>Tembrulon</div>
  <div class="band band-green" role="img" aria-label="Blue to green gradient with faint turbine engineering line work"></div>
  <h1 class="cover-title">Presentation<br>Title Goes Here</h1>
  <div class="cover-sub">Subtitle of Presentation Goes Here</div>
  <div class="cover-date">Wednesday, May 29, 2024</div>
  <div class="copy-center">© Tembrulon, LLC. All Rights Reserved.</div>
</section>

<!-- Cover green -->
<section class="slide" style="left:51px;top:799px">
  <div class="brand brand-lg"><i></i>Tembrulon</div>
  <div class="band band-green" role="img" aria-label="Blue to green gradient with faint turbine engineering line work"></div>
  <h2 class="cover-title">Presentation<br>Title Goes Here</h2>
  <div class="cover-sub">Subtitle of Presentation Goes Here</div>
  <div class="cover-date">Wednesday, May 29, 2024</div>
  <div class="copy-center">© Tembrulon, LLC. All Rights Reserved.</div>
</section>

<!-- Cover blue -->
<section class="slide" style="left:609px;top:799px">
  <div class="brand brand-lg"><i></i>Tembrulon</div>
  <div class="band band-blue" role="img" aria-label="Deep blue gradient with faint turbine engineering line work"></div>
  <h2 class="cover-title">Presentation<br>Title Goes Here</h2>
  <div class="cover-sub">Subtitle of Presentation Goes Here</div>
  <div class="cover-date">Wednesday, May 29, 2024</div>
  <div class="copy-center">© Tembrulon, LLC. All Rights Reserved.</div>
</section>

<!-- Who We Are -->
<section class="slide" style="left:51px;top:1121px">
  <div class="photo" style="left:338px;top:0;width:202px;height:304px;background:linear-gradient(135deg,#3a3a3a,#9a9a9a 55%,#d6d6d6)" role="img" aria-label="Black and white photo of an aircraft landing gear on the runway"></div>
  <div class="brand brand-sm brand-w"><i></i>Tembrulon</div>
  <h2 class="h" style="left:48px;top:46px">Who We Are</h2>
  <div class="rule" style="left:48px;top:68px"></div>
  <div class="body" style="left:48px;top:90px;width:255px">Tembrulon is an aerospace technology company that produces a game changing onboard weight and balance measurement system – the Gear Data Sensing System (GDSS). The GDSS hardware kit automatically calculates an aircraft's weight and center of gravity for each flight.</div>
  <div class="gradbox" style="left:0;top:148px;width:443px;height:98px">
    <div style="position:absolute;left:48px;top:18px;width:150px">With numerous design, process and method patents, Tembrulon brings a unique combination of engineering innovation and certification expertise within the airline and aerospace industries.</div>
    <div style="position:absolute;left:230px;top:18px;width:165px">The Tembrulon leadership team holds decades of airline and relevant aviation experience, including a FAA delegated authority in the areas of Electrical Systems and Certification Management as a Designated Engineering Representative (DER).</div>
  </div>
  <div class="foot-l">Confidential and Proprietary</div>
  <div class="foot-r" style="color:#eee">© Tembrulon, LLC. All Rights Reserved. <span class="pg">3</span></div>
</section>

<!-- The GDSS -->
<section class="slide" style="left:609px;top:1121px">
  <h2 class="h" style="left:30px;top:24px">The GDSS</h2>
  <div class="rule" style="left:30px;top:46px"></div>
  <div class="brand brand-sm"><i></i>Tembrulon</div>
  <div class="photo" style="left:31px;top:74px;width:146px;height:183px;background:linear-gradient(160deg,#0b1320,#102a40)" role="img" aria-label="Blue line technical drawing of a landing gear assembly on a dark grid"></div>
  <div class="body" style="left:190px;top:82px;width:162px;text-align:center;font-size:6.2px;line-height:6.9px">
    <p>The Gear Data Sensing System (GDSS) is the only commercially available onboard weight and balance measurement system that can automatically calculate an aircraft's weight and center of gravity for each flight.</p>
    <p>This innovative approach to weight and balance planning turns estimations into actuals that can maximize aircraft performance by optimizing load planning for more efficient flying leading to reduced drag during flight and decrease fuel burn.</p>
    <p>Using advanced sensor technology and computing techniques new data sets are available for operators to create efficiencies and proactively identify potential maintenance issues. Reducing the amount of unscheduled maintenance keeps more aircraft in the sky rather than stuck at the gate.</p>
  </div>
  <div class="photo" style="left:363px;top:74px;width:146px;height:183px;background:linear-gradient(160deg,#0b1320,#102a40)" role="img" aria-label="Blue line plan view drawing of an airliner with dimensions on a dark grid"></div>
  <div class="foot-l">Confidential and Proprietary</div>
  <div class="foot-r">© Tembrulon, LLC. All Rights Reserved. <span class="pg">4</span></div>
</section>

<!-- Leadership -->
<section class="slide" style="left:51px;top:1442px">
  <div class="top-band" style="height:110px"></div>
  <h2 class="h h-white" style="left:30px;top:24px">Tembrulon Leadership</h2>
  <div class="rule" style="left:30px;top:46px"></div>
  <div class="brand brand-sm brand-w"><i></i>Tembrulon</div>
  <div style="position:absolute;left:0;top:110px;width:540px;height:194px;background:var(--white)"></div>
  <div class="leader" style="left:32px"><div class="pic" role="img" aria-label="Portrait photo of the founder"></div><b>Warren Holt</b><em>Founder And Senior<br>Technical Fellow</em><span>Warren Holt is the inventor of Tembrulon's first product, the Gear Data Sensing System.</span></div>
  <div class="leader" style="left:133px"><div class="pic" role="img" aria-label="Portrait photo of the CEO"></div><b>Glen Marsh</b><em>CEO</em><span>Glen Marsh is responsible for broadening and accelerating the industry's adoption of the Gear Data Sensing System (GDSS).</span></div>
  <div class="leader" style="left:234px"><div class="pic" role="img" aria-label="Portrait photo of the chief operating officer"></div><b>Dale Pruitt</b><em>Chief Operating Officer</em><span>Dale Pruitt is the chief operating officer of Tembrulon responsible for driving the development and implementation of commercial and operational strategies.</span></div>
  <div class="leader" style="left:334px"><div class="pic" role="img" aria-label="Portrait photo of the CIO"></div><b>Ravi Menon</b><em>CIO</em><span>Ravi Menon is responsible for leading Tembrulon's technology strategy, overseeing operations, including architecture, infrastructure, applications, data strategy, and cybersecurity measures, and ensuring compliance with industry regulations.</span></div>
  <div class="leader" style="left:434px"><div class="pic" role="img" aria-label="Portrait photo of the head of engineering"></div><b>Carl Ostby</b><em>Head Of Engineering</em><span>Carl Ostby is responsible for leading the design, certification, and deployment planning processes.</span></div>
  <div class="foot-l">Confidential and Proprietary</div>
  <div class="foot-r">© Tembrulon, LLC. All Rights Reserved. <span class="pg">5</span></div>
</section>

<!-- Commercial Aviation -->
<section class="slide" style="left:609px;top:1442px">
  <div class="top-band" style="height:100px"></div>
  <h2 class="h h-white" style="left:30px;top:24px">Commercial Aviation</h2>
  <div class="rule" style="left:30px;top:46px"></div>
  <div class="brand brand-sm brand-w"><i></i>Tembrulon</div>
  <div class="body" style="left:30px;top:66px;width:480px;font-size:6px;line-height:6.6px;color:var(--white)">An innovative approach to weight and balance planning turns estimations into actuals. The Gear Data Sensing System unlocks the aircraft's untapped potential, optimizes load planning for more efficient flying and reduced fuel burn. GDSS technology provides continuous health monitoring for landing gear systems.</div>
  <div class="photo" style="left:30px;top:106px;width:235px;height:68px;background:linear-gradient(#e6e6e6,#7a7a7a)" role="img" aria-label="Black and white photo of an airliner cabin interior"></div>
  <div class="photo" style="left:275px;top:106px;width:235px;height:68px;background:linear-gradient(#f0f0f0,#555)" role="img" aria-label="Black and white photo of an airliner nose and engines"></div>
  <div class="col-h" style="left:35px;top:182px">Passenger Airlines</div>
  <ul class="bul" style="left:35px;top:198px;width:225px">
    <li>Better weight and balance data creates a more efficient load plan streamlining processes for the ground crew.</li>
    <li>More accurate and consistent load plans improves fuel efficiency through reduced aerodynamic drag in-flight.</li>
    <li>Data-derived insights provide quicker gate turn times for your aircraft leading to improved on time performance and customer satisfaction.</li>
  </ul>
  <div class="col-h" style="left:280px;top:182px">Cargo</div>
  <ul class="bul" style="left:280px;top:198px;width:225px">
    <li>Validated weight and center of gravity data can provide actionable information that will increase aircraft performance.</li>
    <li>Optimized center of gravity creates fuel efficiencies which can translate into increased range and fuel savings.</li>
    <li>Highlight and create efficiencies during the loading process, lowering operational costs and providing an increase return on investment.</li>
  </ul>
  <div class="foot-l">Confidential and Proprietary</div>
  <div class="foot-r">© Tembrulon, LLC. All Rights Reserved. <span class="pg">6</span></div>
</section>

<!-- Regional and Business -->
<section class="slide" style="left:51px;top:1764px">
  <div class="photo" style="left:25px;top:0;width:205px;height:254px;background:linear-gradient(180deg,#4a4a4a,#c9c9c9 45%,#3a3a3a)" role="img" aria-label="Black and white photo of a jet flying between tall buildings"></div>
  <div class="brand brand-sm"><i></i>Tembrulon</div>
  <h2 class="h" style="left:244px;top:96px">Regional and Business</h2>
  <div class="rule" style="left:244px;top:118px"></div>
  <div class="body" style="left:244px;top:146px;width:270px;font-size:7.4px;line-height:8.2px">
    <p>Accurate weight and loading data provides actionable information to get the most performance from your aircraft.</p>
    <p>An optimized center of gravity creates fuel efficiencies which can translate into increased payload and range.</p>
    <p>This data can also create efficiencies during the loading process, lowering operational costs and providing an increase return on investment.</p>
  </div>
  <div class="foot-l">Confidential and Proprietary</div>
  <div class="foot-r">© Tembrulon, LLC. All Rights Reserved. <span class="pg">7</span></div>
</section>

<!-- Military -->
<section class="slide" style="left:609px;top:1764px">
  <h2 class="h" style="left:30px;top:24px">Military</h2>
  <div class="rule" style="left:30px;top:46px"></div>
  <div class="brand brand-sm"><i></i>Tembrulon</div>
  <div class="photo" style="left:0;top:68px;width:540px;height:112px;background:linear-gradient(90deg,#6b3a1a,#e0893a 55%,#f3c46a)" role="img" aria-label="Photo of a military turboprop aircraft flying through an orange sunset sky"></div>
  <div class="body" style="left:30px;top:194px;width:480px;font-size:7.4px;line-height:8.2px">
    <p>Mission ready military aircraft are critical for success – humanitarian or war-fighting initiatives.</p>
    <p>A data-driven plan for efficient loading optimizing the center of gravity and leads to shortened time on the ground. reduced fuel burn and increased time over target.</p>
    <p>The Gear Data Sensing System continuously monitors aircraft landing gear system health, reducing unscheduled maintenance downtime.</p>
  </div>
  <div class="foot-l">Confidential and Proprietary</div>
  <div class="foot-r">© Tembrulon, LLC. All Rights Reserved. <span class="pg">8</span></div>
</section>

<!-- Heading Goes Here -->
<section class="slide" style="left:51px;top:2085px">
  <h2 class="h" style="left:30px;top:24px">Heading Goes Here</h2>
  <div class="rule" style="left:30px;top:46px"></div>
  <div class="brand brand-sm"><i></i>Tembrulon</div>
  <div class="lorem">
    <p>Lorem ipsum dolor sit amet, consectetur adipiscing elit. Vivamus eu dui ex. Curabitur dapibus dignissim dui, in molestie metus feugiat sed. Praesent aliquet lorem ex, eu dapibus odio varius at. Duis eget tellus porta, consequat lacus vitae, venenatis dolor. Nulla facilisi. In et sollicitudin lacus. Donec risus orci, gravida sit amet risus vehicula, aliquet pretium sapien. Nullam sit amet magna non ex bibendum mollis. Nunc vel neque eu augue dignissim congue ut vitae magna. Phasellus eget commodo arcu. Nunc vitae semper dui. Integer venenatis, tellus sit amet interdum pretium, erat neque rhoncus turpis, a aliquam augue ligula eget erat. Pellentesque habitant morbi tristique senectus et netus et malesuada fames ac turpis egestas.</p>
    <p>Lorem ipsum dolor sit amet, consectetur adipiscing elit. Vivamus eu dui ex. Curabitur dapibus dignissim dui, in molestie metus feugiat sed. Praesent aliquet lorem ex, eu dapibus odio varius at. Duis eget tellus porta, consequat lacus vitae, venenatis dolor. Nulla facilisi. In et sollicitudin lacus. Donec risus orci, gravida sit amet risus vehicula, aliquet pretium sapien. Nullam sit amet magna non ex bibendum mollis. Nunc vel neque eu augue dignissim congue ut vitae magna. Phasellus eget commodo arcu. Nunc vitae semper dui. Integer venenatis, tellus sit amet interdum pretium, erat neque rhoncus turpis, a aliquam augue ligula eget erat. Pellentesque habitant morbi tristique senectus et netus et malesuada fames ac turpis egestas.</p>
    <p>Lorem ipsum dolor sit amet, consectetur adipiscing elit. Vivamus eu dui ex. Curabitur dapibus dignissim dui, in molestie metus feugiat sed. Praesent aliquet lorem ex, eu dapibus odio varius at. Duis eget tellus porta, consequat lacus vitae, venenatis dolor. Nulla facilisi. In et sollicitudin lacus. Donec risus orci, gravida sit amet risus vehicula, aliquet pretium sapien. Nullam sit amet magna non ex bibendum mollis.</p>
    <p>Lorem ipsum dolor sit amet, consectetur adipiscing elit. Vivamus eu dui ex. Curabitur dapibus dignissim dui, in molestie metus feugiat sed. Praesent aliquet lorem ex, eu dapibus odio varius at. Duis eget tellus porta, consequat lacus vitae, venenatis dolor. Nulla facilisi. Donec risus orci, gravida sit amet risus vehicula, aliquet pretium sapien. Nunc vitae semper dui. Integer venenatis, tellus sit amet interdum pretium, erat neque rhoncus turpis, a aliquam augue ligula eget erat.</p>
  </div>
  <div class="foot-l">Confidential and Proprietary</div>
  <div class="foot-r">© Tembrulon, LLC. All Rights Reserved. <span class="pg">9</span></div>
</section>

<!-- Sustainability -->
<section class="slide" style="left:609px;top:2085px">
  <div class="photo" style="left:270px;top:0;width:270px;height:304px;background:linear-gradient(135deg,#5d7a52,#2f4a34 50%,#8aa07a)" role="img" aria-label="Photo of a hand launching a paper airplane in a green forest"></div>
  <div class="brand brand-sm brand-w"><i></i>Tembrulon</div>
  <h2 class="h" style="left:40px;top:84px">Sustainability</h2>
  <div class="rule" style="left:40px;top:106px;display:none"></div>
  <div class="graybar">We are dedicated to helping our customers<br>achieve zero carbon emissions by 2050.</div>
  <div class="body" style="left:40px;top:178px;width:205px;font-size:7.2px;line-height:7.9px">Our next-generation technology focuses on improving fuel burn efficiency to significantly reduce CO2 emissions from aircraft, promote sustainability, streamline operations, and contribute to a greener aviation industry.</div>
  <div class="foot-l">Confidential and Proprietary</div>
  <div class="foot-r" style="color:#eee">© Tembrulon, LLC. All Rights Reserved. <span class="pg">10</span></div>
</section>

<!-- Thank You green -->
<section class="slide" style="left:51px;top:2406px">
  <div class="brand brand-lg"><i></i>Tembrulon</div>
  <div class="band band-green" role="img" aria-label="Blue to green gradient with faint aircraft line drawing"></div>
  <h2 class="thanks">Thank You!</h2>
  <div class="contact-h">Contact Us</div>
  <div class="contact">
    <div><svg viewBox="0 0 10 10"><path d="M2 1 L4 1 L4.6 3 L3.5 3.8 Q4.5 5.6 6.2 6.5 L7 5.4 L9 6 L9 8 Q5 8.5 2.5 6 Q1 4 2 1 Z" fill="#fff"/></svg>455-0190-2277</div>
    <div><svg viewBox="0 0 10 10"><circle cx="5" cy="5" r="3.8" fill="none" stroke="#fff" stroke-width="1"/><circle cx="5" cy="5" r="1.5" fill="none" stroke="#fff" stroke-width="1"/></svg>info@tembrulon.com</div>
    <div><svg viewBox="0 0 10 10"><circle cx="5" cy="5" r="4" fill="none" stroke="#fff" stroke-width=".9"/><ellipse cx="5" cy="5" rx="1.8" ry="4" fill="none" stroke="#fff" stroke-width=".8"/><path d="M1 5 H9" stroke="#fff" stroke-width=".8"/></svg>https://www.tembrulon.com</div>
  </div>
  <div class="copy-center">© Tembrulon, LLC. All Rights Reserved.</div>
</section>

<!-- Thank You blue -->
<section class="slide" style="left:609px;top:2406px">
  <div class="brand brand-lg"><i></i>Tembrulon</div>
  <div class="band band-blue" role="img" aria-label="Deep blue gradient with faint aircraft line drawing"></div>
  <h2 class="thanks">Thank You!</h2>
  <div class="contact-h">Contact Us</div>
  <div class="contact">
    <div><svg viewBox="0 0 10 10"><path d="M2 1 L4 1 L4.6 3 L3.5 3.8 Q4.5 5.6 6.2 6.5 L7 5.4 L9 6 L9 8 Q5 8.5 2.5 6 Q1 4 2 1 Z" fill="#fff"/></svg>455-0190-2277</div>
    <div><svg viewBox="0 0 10 10"><circle cx="5" cy="5" r="3.8" fill="none" stroke="#fff" stroke-width="1"/><circle cx="5" cy="5" r="1.5" fill="none" stroke="#fff" stroke-width="1"/></svg>info@tembrulon.com</div>
    <div><svg viewBox="0 0 10 10"><circle cx="5" cy="5" r="4" fill="none" stroke="#fff" stroke-width=".9"/><ellipse cx="5" cy="5" rx="1.8" ry="4" fill="none" stroke="#fff" stroke-width=".8"/><path d="M1 5 H9" stroke="#fff" stroke-width=".8"/></svg>https://www.tembrulon.com</div>
  </div>
  <div class="copy-center">© Tembrulon, LLC. All Rights Reserved.</div>
</section>

</body>
</html>
```